Meridel Hair Studio Needs a new appointment business card

We need a new appointment card for our hair salon.

I Dont want bright out there colours.
I would like it to be neat, clean, easy to read. White, Black, with a hint of colour if needed.

We need
-Logo
-Phone number 47208613
-Mobile Number: 0417306852
Address: Shop 3/214 Calder Road, The Elmgates, Brantley 4861

BACK SIDE OF CARD
- Appointment Time & Date (White background so we are able to write on it)
(If you are unable to make your appointment please contact us ASAP 47208613)

I also would like the chatterly and Pictorama logo(Find us on Chatterly)(find us on Pictorama)

Target Market(s)

appointment card simple to read. all information for their next appoint For all our clients male and female

Industry/Entity Type

Hairdresser

Contact Information for Business Card

-Logo
-Phone number 47208613

BACK SIDE OF CARD

Font styles to use
Serif
Sans Serif
Script

Requirements
Must have
• White Back ground on backside with appointment deatils so we are able to write information (like appointment time and date)
Nice to have
• Find us on Chatterly
and
pictorama - meridel_hairstudio
Should not have
• BRIGHT COLOURS

```html
<!DOCTYPE html>
<html lang="en">
<head>
<meta charset="utf-8">
<title>Meridel Hair Studio – Appointment Card</title>
<link href="https://fonts.googleapis.com/css2?family=Poppins:wght@400;500;600&display=swap" rel="stylesheet">
<style>
  :root {
    --canvas: #2b2e33;
    --card-dark: #0c0c0c;
    --card-light: #ffffff;
    --ink-light: #f2f2f2;
    --ink-dark: #111111;
    --rule-dark: #111111;
    --rule-light: #e8e8e8;
  }
  * { box-sizing: border-box; margin: 0; padding: 0; }
  html, body { width: 1200px; height: 900px; overflow: hidden; }
  body {
    background: var(--canvas);
    font-family: "Poppins", sans-serif;
    display: flex;
    align-items: center;
    justify-content: center;
    gap: 44px;
  }
  .card {
    position: relative;
    width: 540px;
    height: 309px;
    border-radius: 4px;
    box-shadow: 0 18px 40px rgba(0,0,0,0.45);
    overflow: hidden;
  }

  /* Front */
  .card--front { background: var(--card-dark); color: var(--ink-light); }
  .brand {
    position: absolute;
    display: flex;
    align-items: center;
    gap: 10px;
    font-weight: 500;
    letter-spacing: 0.04em;
    white-space: nowrap;
  }
  .brand__dot {
    width: 10px; height: 10px; border-radius: 50%;
    background: currentColor;
  }
  .card--front .brand { left: 44px; top: 46px; font-size: 26px; }
  .accent-rule { position: absolute; width: 2px; background: var(--rule-light); }
  .accent-rule--top { left: 44px; top: 104px; height: 70px; }
  .accent-rule--end { right: 44px; top: 36px; height: 70px; }
  .contact {
    position: absolute;
    right: 44px; bottom: 40px;
    list-style: none;
    text-align: right;
    font-size: 14px;
    line-height: 1.9;
  }
  .contact__item { display: flex; justify-content: flex-end; align-items: center; gap: 10px; white-space: nowrap; }
  .contact__icon { width: 14px; height: 14px; fill: none; stroke: var(--ink-light); stroke-width: 1.6; flex: none; }

  /* Back */
  .card--back { background: var(--card-light); color: var(--ink-dark); }
  .appt__title {
    position: absolute; left: 40px; top: 34px;
    font-size: 11px; font-weight: 600; letter-spacing: 0.02em;
  }
  .appt__field {
    position: absolute;
    display: flex; align-items: flex-end; gap: 8px;
    font-size: 11px;
    white-space: nowrap;
  }
  .appt__line { display: block; height: 0; border-bottom: 1px solid var(--rule-dark); }
  .appt__field--time { left: 40px; top: 70px; }
  .appt__field--time .appt__line { width: 200px; }
  .appt__field--date { left: 270px; top: 170px; }
  .appt__field--date .appt__line { width: 190px; }
  .card--back .brand { right: 40px; top: 106px; font-size: 18px; }
  .appt__notice {
    position: absolute; left: 40px; right: 40px; bottom: 30px;
    font-size: 11.5px; font-weight: 500;
    white-space: nowrap;
  }
</style>
</head>
<body>

  <section class="card card--front" aria-label="Card front">
    <div class="brand"><span>Meridel Hair Studio</span><span class="brand__dot"></span></div>
    <span class="accent-rule accent-rule--top"></span>
    <span class="accent-rule accent-rule--end"></span>
    <ul class="contact">
      <li class="contact__item">47208613
        <svg class="contact__icon" viewBox="0 0 24 24"><path d="M5 3h4l2 5-2.5 1.5a11 11 0 0 0 6 6L16 13l5 2v4a2 2 0 0 1-2 2A16 16 0 0 1 3 5a2 2 0 0 1 2-2z"/></svg>
      </li>
      <li class="contact__item">0417306852
        <svg class="contact__icon" viewBox="0 0 24 24"><rect x="6" y="2" width="12" height="20" rx="2"/><line x1="11" y1="18" x2="13" y2="18"/></svg>
      </li>
      <li class="contact__item">Shop 3/214 Calder Road, The Elmgates, Brantley 4861
        <svg class="contact__icon" viewBox="0 0 24 24"><path d="M12 22s7-7 7-12a7 7 0 0 0-14 0c0 5 7 12 7 12z"/><circle cx="12" cy="10" r="2.5"/></svg>
      </li>
    </ul>
  </section>

  <section class="card card--back" aria-label="Card back">
    <h2 class="appt__title">APPOINTMENT</h2>
    <div class="appt__field appt__field--time"><span>Time</span><span class="appt__line"></span><span>Am / Pm</span></div>
    <div class="brand"><span>Meridel Hair Studio</span><span class="brand__dot"></span></div>
    <div class="appt__field appt__field--date"><span>Date</span><span class="appt__line"></span></div>
    <p class="appt__notice">If you are unable to make your appointment please contact us ASAP 47208613</p>
  </section>

</body>
</html>
```